Brisk Hive 360 Postcard Design, Double-Sided

Please read carefully and see attached. Designers that do not follow these instructions will not be selected. Limit ONE design submission per artist. The ONE design submission shall show both the front and the back designs. Designs must comply with the attached dismensions accounting for the bleed area to prevent designs from being cut off during printing. The attached business card and door tag designs have already been created, printed and are in use. The postcard shall be similar in design to the attached business card and door tag. All of the information that you need is attached. The overall size is 4.12" x 6.12" for the front. The back is different, see attached and scale to match template. I would like the Veteran Owned Business logo added as well. It would also be nice to see my photo incorporated somehow. I like the yellow on the door tag. It helps build contrast and pops out. Again, one design submission per designer that shows both the front and the back.

Target Market(s)

Please read all instructions and see attached.

Industry/Entity Type

Requirements
Must have
• Please read all instructions and see attached.
Nice to have
Should not have

```html
<!DOCTYPE html>
<html lang="en">
<head>
<meta charset="utf-8">
<title>Brisk Hive 360 Handyman Postcard</title>
<link rel="stylesheet" href="https://fonts.googleapis.com/css2?family=Open+Sans:ital,wght@0,400;0,600;0,700;1,800&family=Roboto+Condensed:wght@400&family=Montserrat:wght@400;600&display=swap">
<style>
  :root {
    --stage: #efe7c2;
    --card-dark: #262626;
    --logo-black: #111111;
    --brand-yellow: #f4ec1e;
    --accent-red: #e8202a;
    --paper-white: #f6f6f6;
    --text-light: #f2f2f2;
    --text-dark: #222222;
  }
  * { box-sizing: border-box; margin: 0; padding: 0; }
  html, body { width: 1200px; height: 711px; overflow: hidden; background: var(--stage); }
  .canvas { position: relative; width: 1200px; height: 711px; }

  .postcard { position: absolute; width: 553px; height: 367px; overflow: hidden; }
  .postcard-back { left: 187px; top: 58px; background: var(--paper-white); }
  .postcard-front { left: 462px; top: 296px; background: var(--card-dark); }

  .back-dark-top { position: absolute; left: 0; top: 0; width: 339px; height: 104px; background: var(--card-dark); }
  .back-dark-main { position: absolute; left: 0; top: 104px; width: 302px; height: 196px; background: var(--card-dark); }
  .back-logo-block { position: absolute; left: 339px; top: 0; width: 99px; height: 104px; background: var(--logo-black);
    display: flex; flex-direction: column; align-items: center; justify-content: center; gap: 6px; }
  .logo-dot { width: 10px; height: 10px; border-radius: 50%; background: var(--text-light); }
  .logo-name { font-family: "Open Sans", sans-serif; font-weight: 700; font-size: 12px; color: var(--text-light); text-align: center; line-height: 1.1; }

  .owner-photo { position: absolute; left: 14px; top: 6px; width: 94px; height: 98px;
    background: linear-gradient(180deg, #3a3a3a 0%, #8f9196 55%, #b9bbbe 100%); }

  .web { position: absolute; display: flex; align-items: center; gap: 5px; font-family: "Open Sans", sans-serif;
    font-weight: 800; font-style: italic; color: var(--text-light); white-space: nowrap; transform: translateX(-50%); }
  .web svg { flex: none; }
  .back-web { left: 215px; top: 9px; font-size: 17px; }

  .brand-title { position: absolute; transform: translateX(-50%); font-family: "Open Sans", sans-serif; font-weight: 800;
    font-style: italic; color: var(--brand-yellow); white-space: nowrap; line-height: 1; border-bottom: 2px solid var(--brand-yellow); }
  .brand-sub { position: absolute; transform: translateX(-50%); font-family: "Open Sans", sans-serif; font-weight: 800;
    font-style: italic; color: var(--brand-yellow); white-space: nowrap; line-height: 1; }
  .back-title { left: 215px; top: 43px; font-size: 26px; padding-bottom: 1px; }
  .back-sub { left: 215px; top: 72px; font-size: 21px; }

  .list-heading { position: absolute; font-family: "Open Sans", sans-serif; font-weight: 800; font-style: italic;
    font-size: 17px; color: var(--accent-red); line-height: 1; }
  .list-note { font-family: "Open Sans", sans-serif; font-weight: 400; font-style: normal; font-size: 11px; color: var(--text-light); display: block; margin-top: 2px; }
  .services-heading { left: 16px; top: 112px; }
  .benefits-heading { left: 172px; top: 112px; }
  .bullet-list { position: absolute; list-style: none; font-family: "Roboto Condensed", sans-serif; font-size: 14px; color: var(--text-light); }
  .bullet-list li { height: 21.1px; display: flex; align-items: center; gap: 7px; }
  .bullet-list li::before { content: ""; width: 6px; height: 6px; background: var(--accent-red); transform: rotate(45deg); flex: none; }
  .services-list { left: 17px; top: 192px; transform: translateY(-58px); }
  .benefits-list { left: 173px; top: 205px; transform: translateY(-58px); }
  .vob-badge { position: absolute; left: 200px; top: 235px; width: 46px; height: 44px; border-radius: 50%;
    background: #31478c; border: 3px solid var(--accent-red); }

  .inquire-band { position: absolute; left: 3px; top: 300px; width: 272px; height: 67px; background: var(--paper-white); text-align: center; }
  .inquire-title { font-family: "Open Sans", sans-serif; font-weight: 700; color: var(--text-dark); line-height: 1; }
  .inquire-title .hl { color: var(--accent-red); }
  .back-inquire { font-size: 15px; margin-top: 5px; }
  .contact-line { display: flex; align-items: center; justify-content: center; gap: 4px; font-family: "Montserrat", sans-serif; font-size: 10px; color: var(--text-dark); height: 13px; }

  .front-art { position: absolute; left: 0; top: 0; }
  .front-web { left: 275px; top: 8px; font-size: 16px; }
  .front-title { left: 275px; top: 33px; font-size: 33px; padding-bottom: 1px; }
  .front-sub { left: 275px; top: 73px; font-size: 22px; }
  .front-logo { position: absolute; left: 233px; top: 93px; width: 66px; height: 66px; border-radius: 50%;
    background: var(--logo-black); border: 2px solid var(--text-light); display: flex; align-items: center; justify-content: center; }
  .front-logo .logo-name { font-size: 10px; }
  .front-inquire { position: absolute; left: 0; width: 553px; top: 334px; font-size: 17px; color: var(--text-light); text-align: center; }
  .front-contacts { position: absolute; left: 0; width: 553px; top: 351px; display: flex; justify-content: center; gap: 10px; }
  .front-contacts .contact-line { color: var(--text-light); font-size: 12px; height: 14px; }
</style>
</head>
<body>
<main class="canvas">

  <section class="postcard postcard-back" aria-label="Postcard back">
    <div class="back-dark-top"></div>
    <div class="back-dark-main"></div>
    <div class="owner-photo" role="img" aria-label="Portrait of the business owner in a grey polo shirt"></div>

    <div class="web back-web">
      <svg width="17" height="17" viewBox="0 0 20 20" fill="none" stroke="#f2f2f2" stroke-width="1.4"><circle cx="10" cy="10" r="8.5"/><ellipse cx="10" cy="10" rx="4" ry="8.5"/><path d="M1.5 10h17M3 5.5h14M3 14.5h14M10 1.5v17"/></svg>
      <span>BriskHive360.com</span>
    </div>
    <div class="brand-title back-title">BRISK HIVE 360</div>
    <div class="brand-sub back-sub">HANDYMAN</div>

    <div class="back-logo-block">
      <span class="logo-dot"></span>
      <span class="logo-name">Brisk Hive 360</span>
    </div>

    <h2 class="list-heading services-heading">SERVICES:</h2>
    <ul class="bullet-list services-list">
      <li>Assembly</li>
      <li>Small Repairs</li>
      <li>Wifi / Router Setup</li>
      <li>Wireless Device Setup</li>
      <li>Fabrication</li>
      <li>Hanging Items</li>
      <li>Odd Jobs</li>
    </ul>

    <h2 class="list-heading benefits-heading">BENEFITS<span class="list-note">of using our services:</span></h2>
    <ul class="bullet-list benefits-list">
      <li>Fast Response</li>
      <li>High Quality</li>
      <li>Fair Price</li>
      <li>Veteran Owned</li>
    </ul>
    <div class="vob-badge" role="img" aria-label="Veteran owned business badge"></div>

    <div class="inquire-band">
      <p class="inquire-title back-inquire"><span class="hl">TEXT</span> TO INQUIRE</p>
      <p class="contact-line"><svg width="8" height="8" viewBox="0 0 10 10"><circle cx="5" cy="5" r="5" fill="#f4ec1e"/><path d="M3 2.5l1 1.2-.5.7a4 4 0 0 0 2 2l.7-.5 1.2 1-.6.8C5 7.5 2.5 5 2.3 3.2z" fill="#222"/></svg>(555) 014 2290</p>
      <p class="contact-line"><svg width="8" height="8" viewBox="0 0 10 10"><circle cx="5" cy="5" r="5" fill="#f4ec1e"/><path d="M5 2a2 2 0 0 1 2 2c0 1.5-2 4-2 4S3 5.5 3 4a2 2 0 0 1 2-2z" fill="#222"/></svg>Bayview, Florida</p>
      <p class="contact-line"><svg width="8" height="8" viewBox="0 0 10 10"><circle cx="5" cy="5" r="5" fill="#f4ec1e"/><rect x="2.5" y="3.2" width="5" height="3.6" fill="none" stroke="#222" stroke-width=".8"/><path d="M2.5 3.2L5 5.3l2.5-2.1" fill="none" stroke="#222" stroke-width=".8"/></svg>Service@BriskHive360.com</p>
    </div>
  </section>

  <section class="postcard postcard-front" aria-label="Postcard front">
    <svg class="front-art" width="553" height="367" viewBox="0 0 553 367">
      <defs>
        <linearGradient id="repairTones" x1="0" y1="0" x2="1" y2="1"><stop offset="0" stop-color="#c9a47e"/><stop offset=".5" stop-color="#3f79c4"/><stop offset="1" stop-color="#d9c15a"/></linearGradient>
        <linearGradient id="weldTones" x1="0" y1="0" x2="1" y2="1"><stop offset="0" stop-color="#1c1c1f"/><stop offset=".6" stop-color="#3a3532"/><stop offset="1" stop-color="#c9772f"/></linearGradient>
        <linearGradient id="deviceTones" x1="0" y1="0" x2="1" y2="1"><stop offset="0" stop-color="#5784c2"/><stop offset="1" stop-color="#3f6cb0"/></linearGradient>
      </defs>
      <polygon points="0,92 279,130 553,86 553,342 279,307 0,340" fill="#f6f6f6"/>
      <polygon points="0,99 175,125 175,313 0,330" fill="url(#repairTones)" role="img" aria-label="Photo of a man measuring a rod at a workbench with tools"/>
      <polygon points="182,128 370,127 370,312 279,304 182,312" fill="url(#weldTones)" role="img" aria-label="Photo of a worker grinding metal with sparks"/>
      <polygon points="375,126 553,91 553,335 375,313" fill="url(#deviceTones)" role="img" aria-label="Illustration of a smart speaker with a watch and phone connected wirelessly"/>
      <polyline points="17,84 279,124 536,82" fill="none" stroke="#f4ec1e" stroke-width="3"/>
      <polyline points="20,350 279,306 536,350" fill="none" stroke="#f4ec1e" stroke-width="3"/>
    </svg>

    <div class="web front-web">
      <svg width="17" height="17" viewBox="0 0 20 20" fill="none" stroke="#f2f2f2" stroke-width="1.4"><circle cx="10" cy="10" r="8.5"/><ellipse cx="10" cy="10" rx="4" ry="8.5"/><path d="M1.5 10h17M3 5.5h14M3 14.5h14M10 1.5v17"/></svg>
      <span>BriskHive360.com</span>
    </div>
    <div class="brand-title front-title">BRISK HIVE 360</div>
    <div class="brand-sub front-sub">HANDYMAN</div>

    <div class="front-logo"><span class="logo-name">Brisk Hive 360</span></div>

    <p class="inquire-title front-inquire"><span class="hl">TEXT</span> TO INQUIRE</p>
    <div class="front-contacts">
      <p class="contact-line"><svg width="11" height="11" viewBox="0 0 10 10"><circle cx="5" cy="5" r="5" fill="#f2f2f2"/><path d="M3 2.5l1 1.2-.5.7a4 4 0 0 0 2 2l.7-.5 1.2 1-.6.8C5 7.5 2.5 5 2.3 3.2z" fill="#262626"/></svg>(555) 014 2290</p>
      <p class="contact-line"><svg width="11" height="11" viewBox="0 0 10 10"><circle cx="5" cy="5" r="5" fill="#f2f2f2"/><path d="M5 2a2 2 0 0 1 2 2c0 1.5-2 4-2 4S3 5.5 3 4a2 2 0 0 1 2-2z" fill="#262626"/></svg>Bayview, Florida</p>
      <p class="contact-line"><svg width="11" height="11" viewBox="0 0 10 10"><circle cx="5" cy="5" r="5" fill="#f2f2f2"/><rect x="2.5" y="3.2" width="5" height="3.6" fill="none" stroke="#262626" stroke-width=".8"/><path d="M2.5 3.2L5 5.3l2.5-2.1" fill="none" stroke="#262626" stroke-width=".8"/></svg>Service@BriskHive360.com</p>
    </div>
  </section>

</main>
</body>
</html>
```